Ashcombe Heritage Guild Harvest Lantern Days Event Flyer - Historic Event

I need a flyer about the Ashcombe Heritage Guild's Harvest Lantern Days event October 8th and 9th. The centerpiece of Harvest Lantern Days is Civil War reenactments. I want the flyer to include the schedule of events and be eye catching on area bulletin boards. Our website is www.ashcombeheritageguild.org for more information and pictures. The website for the Calder Ridge Rangers reenactors is http://www.calderridgerangers.com/.

Target Market(s)

Our target market is middle ages (35-70) families and couples. Most are history buffs, especially about the Civil War.

Industry/Entity Type

Non-Profit

Font styles to use
Serif
Decorative
Script

Requirements
Must have
• The flyer must include the majority of the schedule attached - especially the battle times, museums, and anything including food.The dance on Saturday night is also important. The bottom of the flyer MUST say "Paid in part by Quillan County Visitor Levy Board"
Nice to have
• Pictures

```html
<!DOCTYPE html>
<html lang="en">
<head>
<meta charset="utf-8">
<title>Ashcombe Heritage Guild – Harvest Lantern Days Flyer</title>
<link rel="stylesheet" href="https://fonts.googleapis.com/css2?family=Rye&family=Libre+Baskerville:ital,wght@0,400;0,700;1,400;1,700&family=Old+Standard+TT:ital,wght@0,400;0,700;1,400&family=Open+Sans:wght@700&display=swap">
<style>
  :root {
    --page-bg: #efe7dc;
    --maroon: #7a1f3d;
    --maroon-dark: #4a0f22;
    --parchment-light: #e9d39a;
    --parchment-mid: #d4b46a;
    --parchment-edge: #8a4a1c;
    --ink: #6d1a35;
    --tape: rgba(255,255,255,0.7);
  }
  * { box-sizing: border-box; margin: 0; padding: 0; }
  html, body { width: 1087px; height: 1200px; overflow: hidden; background: var(--page-bg); }
  .flyer {
    position: absolute; left: 118px; top: 20px; width: 850px; height: 1160px;
    background:
      radial-gradient(ellipse at 50% 45%, var(--parchment-light) 0%, var(--parchment-mid) 62%, #b0793a 88%, var(--parchment-edge) 100%);
    box-shadow: 0 6px 24px rgba(60,30,10,0.25);
    overflow: hidden;
    color: var(--ink);
  }
  .title-block { position: absolute; left: 40px; top: 46px; width: 640px; }
  .rule { height: 3px; background: var(--maroon); width: 100%; }
  .title {
    font-family: "Rye", serif; color: var(--maroon);
    -webkit-text-stroke: 1px var(--maroon-dark);
    text-shadow: 1px 1px 0 rgba(255,240,200,0.6);
    line-height: 1.05; white-space: nowrap;
  }
  .title.line-one { font-size: 36px; margin: 12px 0 8px; }
  .title.line-two { font-size: 34px; margin: 10px 0 14px 30px; }
  .dates {
    position: absolute; right: 40px; top: 58px; text-align: right;
    font-family: "Open Sans", sans-serif; font-weight: 700; color: var(--maroon);
    font-size: 30px; line-height: 1.1;
  }
  .dates sup { font-size: 16px; }
  .photo {
    position: absolute; width: 290px; height: 250px;
    border: 10px solid var(--maroon); border-radius: 10px;
    outline: 4px solid #f4efe6; outline-offset: -14px;
  }
  .photo.cabin { left: 70px; top: 250px; transform: rotate(-3deg);
    background: linear-gradient(160deg, #7fb04a 0%, #a4a39a 45%, #6b4a2e 80%, #4f7a2c 100%); }
  .photo.pavilion { left: 470px; top: 200px; transform: rotate(3deg);
    background: linear-gradient(170deg, #ece6d8 0%, #c9b08a 40%, #7a4a26 70%, #3e2c20 100%); }
  .tape { position: absolute; width: 80px; height: 20px; background: var(--tape); }
  .tape.tl { left: -30px; top: -6px; transform: rotate(-40deg); }
  .tape.br { right: -30px; bottom: -6px; transform: rotate(-40deg); }
  .events-heading {
    position: absolute; left: 0; width: 100%; top: 540px; text-align: center;
    font-family: "Rye", serif; font-size: 52px; color: var(--maroon);
  }
  .events-rule { position: absolute; left: 220px; width: 410px; top: 612px; height: 2px; background: var(--maroon); }
  .day { position: absolute; top: 640px; font-family: "Old Standard TT", serif; }
  .day.saturday { left: 40px; width: 410px; }
  .day.sunday { left: 470px; width: 345px; }
  .day-title {
    font-family: "Libre Baskerville", serif; font-weight: 700; font-size: 22px; white-space: nowrap;
    color: var(--maroon); border-bottom: 2px solid var(--maroon); padding-bottom: 4px; margin-bottom: 10px;
  }
  .day-note { font-family: "Libre Baskerville", serif; font-style: italic; font-weight: 700; font-size: 17px; color: var(--maroon); margin-bottom: 10px; line-height: 1.3; }
  .schedule { list-style: none; }
  .schedule li { position: relative; padding-left: 18px; font-size: 17px; line-height: 1.3; margin-bottom: 7px; color: var(--ink); }
  .schedule li::before { content: ""; position: absolute; left: 2px; top: 8px; width: 7px; height: 7px; border-radius: 50%; background: var(--maroon); }
  .sponsor-band {
    position: absolute; left: 470px; width: 345px; bottom: 50px; padding: 14px 16px;
    background: var(--maroon); border: 3px solid #f4efe6; border-radius: 40px;
    font-family: "Open Sans", sans-serif; font-weight: 700; color: #fff; text-align: center;
    font-size: 22px; line-height: 1.2;
  }
</style>
</head>
<body>
  <main class="flyer">
    <header class="title-block">
      <div class="rule"></div>
      <h1 class="title line-one">Ashcombe Heritage Guild's</h1>
      <div class="rule"></div>
      <h2 class="title line-two">Harvest Lantern Days event</h2>
      <div class="rule"></div>
    </header>
    <p class="dates">8<sup>th</sup> &amp; 9<sup>th</sup><br>October</p>

    <div class="photo cabin" role="img" aria-label="Photo of a weathered log cabin among green trees">
      <span class="tape tl"></span><span class="tape br"></span>
    </div>
    <div class="photo pavilion" role="img" aria-label="Photo of visitors under a canvas-roofed timber pavilion">
      <span class="tape tl"></span><span class="tape br"></span>
    </div>

    <h2 class="events-heading">Events &amp; Time</h2>
    <div class="events-rule"></div>

    <section class="day saturday">
      <h3 class="day-title">Saturday, October 8th, 2016</h3>
      <p class="day-note">Through the Day – Demonstrations and Speakers in various locations</p>
      <ul class="schedule">
        <li>10:00 AM – Battle by Calder Ridge Rangers, sponsored in part by Hollis Corner Market</li>
        <li>11:30-1:00 – Chicken Biscuit Bake at Town Hall – Free Will Donation</li>
        <li>Afternoon – Trolley and Buggy Rides</li>
        <li>1:00-4:00 Museums Opens</li>
        <li>1:30-2:00 Birthday Cake on Marlow House Front Porch, cake donated by Pennant Grocers – Riverbend City</li>
        <li>2:00 Battle by Calder Ridge Rangers</li>
        <li>3:00 Sightseeing Cruise on the Spirit of Ashcombe</li>
        <li>6:00-? Dance at Town Hall with Lamplight Band, sponsored by Dr. Marsh</li>
      </ul>
    </section>

    <section class="day sunday">
      <h3 class="day-title">Sunday, October 9th, 2016</h3>
      <ul class="schedule">
        <li>12:30 PM Parade on Main Street</li>
        <li>Afternoon – Buggy &amp; Trolley Rides</li>
        <li>1:00-4:00 Museums Open</li>
        <li>1:30 Battle by Calder Ridge Rangers</li>
        <li>2:00 Pie Reception at Ashcombe Depot and Railroad History Museum</li>
        <li>3:00 Sightseeing Cruise</li>
      </ul>
    </section>

    <footer class="sponsor-band">Paid in part by Quillan<br>County Visitor Levy Board</footer>
  </main>
</body>
</html>
```